Brannock Bay Ferry and Haulage

Need to redesign our business cards to relay that we do freight logistics and water taxi service. We also work with gov. agencies doing environmental clean up, oil spill response, remote site construction and work with many of the air taxi and helicopter services on Kodiak Island. Out website is www.brannockbayferry.com to get a better idea of what we do.

Contact Information for Business Card

I have a previous business card but it just has the logo on the front, and a sunset picture on the back with the contact info. It does not relay what we do and what we can help with. I like a simple straight forward design over a busy one.

Colors
3176b5
0455a3
cfdfed

Requirements
Must have
• logo, email, website, phone number

```html
<!DOCTYPE html>
<html lang="en">
<head>
<meta charset="utf-8">
<title>Brannock Bay Ferry and Haulage – Business Card</title>
<link rel="stylesheet" href="https://fonts.googleapis.com/css2?family=Poppins:wght@400;500&display=swap">
<style>
  :root {
    --page-bg: #e9e9e9;
    --card-white: #ffffff;
    --brand-blue: #0530a8;
    --sky-blue: #5ab4e0;
    --sun-orange: #f5a10f;
    --text-grey: #454545;
    --on-dark: #ffffff;
  }
  * { box-sizing: border-box; margin: 0; padding: 0; }
  html, body {
    width: 1125px; height: 1200px; overflow: hidden;
    background: var(--page-bg);
    font-family: "Poppins", sans-serif;
  }
  .canvas { position: relative; width: 1125px; height: 1200px; }
  .card {
    position: absolute; left: 153px; width: 826px; height: 472px;
  }
  .card-front { top: 103px; background: var(--card-white); }
  .card-back { top: 637px; background: var(--brand-blue); }

  .brand-name {
    position: absolute; right: 70px; top: 170px;
    text-align: right;
    color: var(--brand-blue);
    font-weight: 500; font-size: 30px; line-height: 1.15;
    letter-spacing: 0.5px;
  }
  .accent-bar {
    position: absolute; left: 0; top: 281px;
    width: 14px; height: 48px; background: var(--sky-blue);
  }
  .person-name {
    position: absolute; left: 49px; top: 278px;
    color: var(--brand-blue); font-weight: 500; font-size: 28px; line-height: 1.1;
  }
  .person-title {
    position: absolute; left: 49px; top: 310px;
    color: var(--sun-orange); font-weight: 500; font-size: 20px; line-height: 1.1;
  }
  .contact-list {
    position: absolute; left: 49px; top: 360px; list-style: none;
  }
  .contact-item {
    display: flex; align-items: center; gap: 12px;
    height: 26.5px;
    color: var(--text-grey); font-size: 19.5px; font-weight: 400;
  }
  .contact-icon { width: 19px; height: 19px; flex: none; }

  .back-brand {
    position: absolute; left: 0; right: 0; top: 190px;
    text-align: center;
    color: var(--on-dark); font-weight: 500; font-size: 38px; line-height: 1.2;
  }
  .back-url {
    position: absolute; left: 0; right: 0; top: 403px;
    text-align: center;
    color: var(--on-dark); font-size: 18px; letter-spacing: 6px;
  }
</style>
</head>
<body>
<div class="canvas">
  <section class="card card-front">
    <div class="brand-name">Brannock Bay<br>Ferry and Haulage</div>
    <div class="accent-bar"></div>
    <div class="person-name">ELENA VARGA</div>
    <div class="person-title">CEO/FOUNDER</div>
    <ul class="contact-list">
      <li class="contact-item">
        <svg class="contact-icon" viewBox="0 0 24 24"><path fill="var(--brand-blue)" d="M6.6 10.8c1.4 2.8 3.8 5.1 6.6 6.6l2.2-2.2c.3-.3.7-.4 1-.2 1.1.4 2.3.6 3.6.6.6 0 1 .4 1 1V20c0 .6-.4 1-1 1C10.6 21 3 13.4 3 4c0-.6.4-1 1-1h3.5c.6 0 1 .4 1 1 0 1.3.2 2.5.6 3.6.1.3 0 .7-.2 1z"/></svg>
        <span>907 555 0148</span>
      </li>
      <li class="contact-item">
        <svg class="contact-icon" viewBox="0 0 24 24"><rect x="2" y="5" width="20" height="14" fill="var(--brand-blue)"/><path d="M3 6l9 7 9-7" fill="none" stroke="#fff" stroke-width="1.8"/></svg>
        <span>elena@brannockbayferry.com</span>
      </li>
      <li class="contact-item">
        <svg class="contact-icon" viewBox="0 0 24 24"><circle cx="12" cy="12" r="10" fill="var(--brand-blue)"/><path d="M2 12h20M12 2c3 3 3 17 0 20M12 2c-3 3-3 17 0 20" fill="none" stroke="#fff" stroke-width="1.4"/></svg>
        <span>www.brannockbayferry.com</span>
      </li>
    </ul>
  </section>

  <section class="card card-back">
    <div class="back-brand">Brannock Bay<br>Ferry and Haulage</div>
    <div class="back-url">www.brannockbayferry.com</div>
  </section>
</div>
</body>
</html>
```